Solar company mail box flyer design

We are a solar installation company and we currently need a DL flyer design for mailbox distribution. The front page need to mention that the government rebate is going to be reduced from the first day of the next year. Also, it need to mentioned that $100 discount available for any customer who show us this flyer. We will also need to have some solar panels and inverters demonstrated on the front page.

I have attached some similar flyers for reference purpose.

```html
<!DOCTYPE html>
<html lang="en">
<head>
<meta charset="utf-8">
<title>Brightway Solar – DL Flyer</title>
<link href="https://fonts.googleapis.com/css2?family=Source+Sans+3:wght@400;600;700&display=swap" rel="stylesheet">
<style>
  :root {
    --blue-deep: #1668b8;
    --blue-mid: #1c8fd6;
    --blue-light: #2fb4ea;
    --brand-blue: #1f4fa0;
    --orange: #f7a21b;
    --orange-deep: #f08a12;
    --sky-pale: #eaf4fb;
    --white: #ffffff;
    --ink: #3d4652;
  }
  * { margin: 0; padding: 0; box-sizing: border-box; }
  html, body { width: 699px; height: 1200px; overflow: hidden; background: #f2f2f2; }
  .flyer {
    position: relative;
    width: 699px;
    height: 1200px;
    overflow: hidden;
    background: var(--white);
    font-family: "Source Sans 3", "Myriad Pro", sans-serif;
  }
  .flyer-art { position: absolute; inset: 0; }
  .brand {
    position: absolute;
    left: 40px; top: 60px;
    width: 232px;
    text-align: center;
    color: var(--brand-blue);
    font-weight: 700;
  }
  .brand-dot {
    display: block;
    width: 90px; height: 90px;
    margin: 0 auto 14px;
    border-radius: 50%;
    background: var(--orange);
  }
  .brand-name { font-size: 34px; line-height: 1.05; letter-spacing: 0.5px; }
  .brand-name span { display: block; font-size: 48px; }
  .offer {
    position: absolute;
    left: 494px; top: 263px;
    width: 172px;
    text-align: center;
    color: var(--white);
  }
  .offer-amount { font-size: 44px; font-weight: 700; line-height: 1; margin-top: 28px; }
  .offer-note { font-size: 23px; line-height: 1.2; margin-top: 6px; }
  .headline {
    position: absolute;
    left: 0; right: 0; top: 412px;
    text-align: center;
    color: var(--white);
    font-size: 56px;
    font-weight: 700;
    letter-spacing: -0.5px;
  }
  .divider {
    position: absolute;
    left: 38px; top: 490px;
    width: 629px; height: 2px;
    background: linear-gradient(90deg, rgba(247,162,27,0), var(--orange) 15%, var(--orange) 85%, rgba(247,162,27,0));
  }
  .intro {
    position: absolute;
    left: 30px; right: 30px; top: 503px;
    text-align: center;
    color: var(--white);
    font-size: 23.5px;
    line-height: 1.17;
  }
  .benefits {
    position: absolute;
    left: 48px; top: 772px;
    width: 620px;
    list-style: none;
    color: var(--ink);
    font-size: 25px;
    line-height: 1.1;
  }
  .benefits li {
    position: relative;
    padding-left: 66px;
    margin-bottom: 29px;
  }
  .benefits svg { position: absolute; left: 0; top: 4px; }
  .contact {
    position: absolute;
    left: 0; right: 0; top: 1068px;
    text-align: center;
    color: var(--white);
  }
  .contact-cta { font-size: 29px; font-weight: 600; }
  .contact-phone {
    display: inline-flex;
    align-items: center;
    gap: 10px;
    color: var(--orange);
    font-size: 40px;
    font-weight: 600;
    line-height: 1.1;
    margin-top: 4px;
  }
  .contact-web { font-size: 27px; font-weight: 600; margin-top: 4px; }
</style>
</head>
<body>
<main class="flyer">
  <svg class="flyer-art" width="699" height="1200" viewBox="0 0 699 1200" xmlns="http://www.w3.org/2000/svg">
    <defs>
      <linearGradient id="heroPhoto" x1="0" y1="0" x2="1" y2="1">
        <stop offset="0" stop-color="#ffffff"/>
        <stop offset="0.45" stop-color="#d9ecf8"/>
        <stop offset="0.75" stop-color="#5d8fd4"/>
        <stop offset="1" stop-color="#2e63b8"/>
      </linearGradient>
      <linearGradient id="grassTone" x1="0" y1="0" x2="1" y2="0">
        <stop offset="0" stop-color="#a8cf4a"/>
        <stop offset="1" stop-color="#a8cf4a" stop-opacity="0"/>
      </linearGradient>
      <linearGradient id="skyPhoto" x1="0" y1="0" x2="0" y2="1">
        <stop offset="0" stop-color="#cfe5f5"/>
        <stop offset="0.6" stop-color="#f2f8fc"/>
        <stop offset="1" stop-color="#dfe6ee"/>
      </linearGradient>
      <linearGradient id="bandBlue" x1="0" y1="0" x2="0" y2="1">
        <stop offset="0" stop-color="var(--blue-light)"/>
        <stop offset="0.5" stop-color="var(--blue-mid)"/>
        <stop offset="1" stop-color="var(--blue-deep)"/>
      </linearGradient>
      <linearGradient id="footBlue" x1="0" y1="0" x2="0" y2="1">
        <stop offset="0" stop-color="var(--blue-light)"/>
        <stop offset="1" stop-color="var(--blue-deep)"/>
      </linearGradient>
    </defs>

    <g role="img" aria-label="Photo of rooftop solar panels angled toward a bright sky over green grass">
      <rect x="0" y="0" width="699" height="420" fill="url(#heroPhoto)"/>
      <rect x="0" y="300" width="260" height="100" fill="url(#grassTone)"/>
    </g>
    <g role="img" aria-label="Soft photo of clouds and solar panels fading into the background">
      <rect x="0" y="640" width="699" height="440" fill="url(#skyPhoto)"/>
    </g>

    <path class="wave-orange" d="M360,395 C500,420 620,410 699,360 L699,440 C600,470 480,455 360,420 Z" fill="var(--orange)"/>
    <path class="band-blue" d="M0,376 C140,352 300,360 430,398 C550,432 640,415 699,392 L699,560 C600,600 500,660 380,690 C250,720 120,690 0,668 Z" fill="url(#bandBlue)"/>
    <path class="wave-orange" d="M0,668 C120,690 250,720 380,690 C500,660 600,600 699,560 L699,585 C600,625 500,690 380,712 C250,736 120,712 0,704 Z" fill="var(--orange)"/>

    <g role="img" aria-label="Product photo of string inverters in blue, red and grey housings">
      <circle cx="364" cy="672" r="90" fill="#ffffff" stroke="var(--orange)" stroke-width="5"/>
      <circle cx="364" cy="672" r="80" fill="#e6e9ee"/>
    </g>
    <g role="img" aria-label="Product photo of a white wall-mounted inverter">
      <circle cx="580" cy="672" r="90" fill="#ffffff" stroke="var(--orange)" stroke-width="5"/>
      <circle cx="580" cy="672" r="80" fill="#eef0f3"/>
    </g>

    <path class="wave-orange" d="M260,1062 C450,1060 590,1030 699,970 L699,1030 C590,1070 430,1080 260,1070 Z" fill="var(--orange)"/>
    <path class="band-blue" d="M0,1050 C200,1034 420,1068 560,1050 C620,1042 670,1025 699,1012 L699,1200 L0,1200 Z" fill="url(#footBlue)"/>

    <g class="offer-badge">
      <circle cx="580" cy="343" r="84" fill="var(--orange)" stroke="var(--orange)" stroke-width="16" stroke-dasharray="0 15.5" stroke-linecap="round"/>
      <circle cx="580" cy="343" r="78" fill="var(--orange-deep)"/>
      <circle cx="580" cy="343" r="72" fill="var(--orange)"/>
    </g>
  </svg>

  <div class="brand">
    <span class="brand-dot"></span>
    <div class="brand-name">BRIGHTWAY<span>SOLAR</span></div>
  </div>

  <div class="offer">
    <div class="offer-amount">$100</div>
    <div class="offer-note">discount<br>with this flyer</div>
  </div>

  <h1 class="headline">WHY WAIT?</h1>
  <div class="divider"></div>
  <p class="intro">Going solar has never been easier and more affordable. Call us today for your FREE solar evaluation and get started with a brighter future tomorrow.</p>

  <ul class="benefits">
    <li>
      <svg width="38" height="38" viewBox="0 0 38 38"><circle cx="19" cy="19" r="16" fill="none" stroke="#f7a21b" stroke-width="3"/><path d="M11 19 L17 25 L30 10" fill="none" stroke="#f7a21b" stroke-width="3.5" stroke-linecap="round" stroke-linejoin="round"/></svg>
      Did you know you can save at least $400 a quarter on your power bill with solar?
    </li>
    <li>
      <svg width="38" height="38" viewBox="0 0 38 38"><circle cx="19" cy="19" r="16" fill="none" stroke="#f7a21b" stroke-width="3"/><path d="M11 19 L17 25 L30 10" fill="none" stroke="#f7a21b" stroke-width="3.5" stroke-linecap="round" stroke-linejoin="round"/></svg>
      Electricity company or back in your pocket? Choice is yours!
    </li>
    <li>
      <svg width="38" height="38" viewBox="0 0 38 38"><circle cx="19" cy="19" r="16" fill="none" stroke="#f7a21b" stroke-width="3"/><path d="M11 19 L17 25 L30 10" fill="none" stroke="#f7a21b" stroke-width="3.5" stroke-linecap="round" stroke-linejoin="round"/></svg>
      Government rebate is going to be reduced from the first day of the next year
    </li>
  </ul>

  <div class="contact">
    <div class="contact-cta">Call for a FREE Quote</div>
    <div class="contact-phone">
      <svg width="38" height="38" viewBox="0 0 38 38"><circle cx="19" cy="19" r="16.5" fill="none" stroke="#f7a21b" stroke-width="3"/><path d="M13 10 C11 11 10 13 11 16 C13 22 17 26 23 28 C26 29 28 27 29 25 L25 21 L22 23 C19 22 16 19 15 16 L17 13 Z" fill="#f7a21b"/></svg>
      1300 555 018
    </div>
    <div class="contact-web">www.brightwaysolar.com.au</div>
  </div>
</main>
</body>
</html>
```